Flock and co fleece works pty ltd

We are sheep shearing contractors,we are looking for a simple design business card, with a drawing like picture of a Australian sheep on it, then just standard details, name, phone, email, po box.
We would like double sided, with 2 lines of wiriting on the back, no bright colours please.
We like black and white, doesn't have to be too serious, however nothing to far left of cwntre.
On the back of the card we would like professional shearing contract offering full contract team.
Can use use the symbol & in the name instead of and.

Target Market(s)

Sheep farmers, target males from age 20 and up

Contact Information for Business Card

Company name flock and co fleece works pty ltd
Darren holloway 0491352706, po box 4071 sale vic 3853,
Email flockandcofleece@mailbarn.example, gippsland shearing contractor

Font styles to use
Serif

Colors

Designer to choose only greyscale colors for use in the design.

Requirements
Nice to have
• Simple design

```html
<!DOCTYPE html>
<html lang="en">
<head>
<meta charset="utf-8">
<title>Flock and co fleece works pty ltd – Business Card</title>
<link rel="stylesheet" href="https://fonts.googleapis.com/css2?family=Libre+Caslon+Text:ital,wght@0,700;1,400&family=Oleo+Script:wght@700&family=Lato:wght@400&display=swap">
<style>
  :root {
    --ink: #111111;
    --ink-soft: #555555;
    --paper: #ffffff;
    --grey-light: #f2f2f2;
    --grey-mid: #c4c4c4;
    --grey-edge: #8a8a8a;
    --band: #d9d9d9;
    --night: #000000;
  }
  * { margin: 0; padding: 0; box-sizing: border-box; }
  html, body {
    width: 813px; height: 1200px; overflow: hidden;
    background: var(--paper);
  }
  .sheet { position: relative; width: 813px; height: 1200px; }

  .card { position: absolute; left: 0; width: 813px; overflow: hidden; }

  /* Front */
  .card-front {
    top: 0; height: 543px;
    background: radial-gradient(ellipse 62% 70% at 50% 42%, var(--grey-light) 0%, var(--grey-mid) 68%, var(--grey-edge) 100%);
  }
  .company-name {
    position: absolute; left: 90px; right: 90px; top: 150px;
    font-family: "Libre Caslon Text", Georgia, serif;
    font-weight: 700; font-size: 44px; line-height: 1.15;
    color: var(--ink); text-align: center;
  }
  .contact-name {
    position: absolute; left: 0; right: 0; top: 306px;
    font-family: "Oleo Script", Georgia, serif;
    font-weight: 700; font-size: 50px;
    color: var(--ink-soft); text-align: center;
  }
  .contact-details {
    position: absolute; left: 0; right: 0; top: 375px;
    font-family: "Lato", Arial, sans-serif;
    font-size: 23px; line-height: 36px;
    color: var(--ink); text-align: center;
    list-style: none;
  }

  /* Back */
  .card-back {
    top: 652px; height: 548px;
    background: radial-gradient(ellipse 70% 75% at 50% 30%, var(--grey-light) 0%, var(--grey-mid) 65%, var(--grey-edge) 100%);
  }
  .back-shapes { position: absolute; inset: 0; }
  .shearer-art {
    position: absolute; left: 72px; top: 82px; width: 270px; height: 310px;
    background: radial-gradient(ellipse at 45% 45%, #6e6e6e 0%, #3a3a3a 60%, rgba(40,40,40,0.3) 100%);
    border-radius: 40% 45% 20% 30%;
  }
  .service-title {
    position: absolute; left: 345px; width: 340px; top: 66px;
    font-family: "Libre Caslon Text", Georgia, serif;
    font-weight: 700; font-size: 45px; line-height: 57px;
    color: var(--ink); text-align: center;
    z-index: 1;
  }
  .service-offer {
    position: absolute; left: 0; right: 0; top: 432px;
    font-family: "Libre Caslon Text", Georgia, serif;
    font-style: italic; font-weight: 400; font-size: 44px;
    color: var(--paper); text-align: center;
  }
</style>
</head>
<body>
<main class="sheet">
  <section class="card card-front" aria-label="Card front">
    <h1 class="company-name">Flock and co fleece works pty ltd</h1>
    <p class="contact-name">Darren Holloway</p>
    <ul class="contact-details">
      <li>Tel: 0491352706</li>
      <li>PO Box 4071 Sale Victoria 3853</li>
      <li>Email: flockandcofleece@mailbarn.example</li>
    </ul>
  </section>

  <section class="card card-back" aria-label="Card back">
    <svg class="back-shapes" width="813" height="548" viewBox="0 0 813 548" aria-hidden="true">
      <path d="M0 270 C 200 330, 420 350, 560 300 C 660 262, 740 232, 813 222 L813 548 L0 548 Z" fill="var(--band)"/>
      <path d="M0 300 C 200 380, 420 400, 580 345 C 680 310, 750 282, 813 275 L813 548 L0 548 Z" fill="var(--night)"/>
    </svg>
    <div class="shearer-art" role="img" aria-label="Woodcut-style illustration of a shearer in a hat shearing a sheep"></div>
    <h2 class="service-title">Professional Gippsland Shearing Contractor</h2>
    <p class="service-offer">Offering a full contract team</p>
  </section>
</main>
</body>
</html>
```